Retail Jewelry Business Card Design Project

We are in need of a new business card design for a retail jewelry store. This store is in the business of fine jewelry including but not specific to bridal jewelry, diamonds, designer jewelry and watches.

This store has been in business for 20 years but continues to strive for a modern professional appeal. The main colors use for this business are a royal blue, white and silver.

Target Market(s)

Target market is ages 18-50

Industry/Entity Type

Jewelry

Requirements
Must have
• Sales Person Name
Sales Person Email Address

Store Address
Store Phone
Website

Standard business card size. No odd shapes or sizes.
Nice to have
• Overall modern feel for card.

We have thought that a design with a nice feature of the logo on the back of the card would be nice but open to ideas.
Should not have
• No specific images of jewelry should be used.

```html
<!DOCTYPE html>
<html lang="en">
<head>
<meta charset="utf-8">
<title>Marlowe Reed Fine Jewelry – Business Card</title>
<link rel="stylesheet" href="https://fonts.googleapis.com/css2?family=Roboto:wght@400&display=swap">
<style>
  :root {
    --page-bg: #e9e9ec;
    --card-edge: #3f32a0;
    --card-glow: #7465c4;
    --card-base: #4b3cb0;
    --ink: #ffffff;
    --silver: rgba(220, 215, 245, 0.55);
    --monogram: rgba(40, 28, 120, 0.28);
  }
  * { box-sizing: border-box; margin: 0; padding: 0; }
  html, body {
    width: 1200px;
    height: 900px;
    overflow: hidden;
    background: var(--page-bg);
  }
  .sheet {
    width: 1200px;
    height: 900px;
    display: flex;
    flex-direction: column;
    align-items: center;
    justify-content: center;
    gap: 40px;
  }
  .card {
    position: relative;
    width: 700px;
    height: 400px;
    background: radial-gradient(ellipse at 45% 40%, var(--card-glow) 0%, var(--card-base) 55%, var(--card-edge) 100%);
    color: var(--ink);
    font-family: "Roboto", Arial, sans-serif;
    overflow: hidden;
    box-shadow: 0 4px 14px rgba(0, 0, 0, 0.18);
  }
  .card-front {
    display: flex;
    flex-direction: column;
    align-items: center;
    justify-content: center;
  }
  .brand-name {
    font-size: 40px;
    font-weight: 400;
    letter-spacing: 4px;
    text-transform: uppercase;
    color: var(--ink);
  }
  .brand-rule {
    width: 460px;
    height: 2px;
    margin-top: 22px;
    background: var(--silver);
  }
  .card-back {
    display: flex;
    flex-direction: column;
    align-items: center;
    justify-content: center;
    text-align: center;
    text-transform: uppercase;
  }
  .back-mark {
    position: absolute;
    left: 50%;
    top: 50%;
    width: 300px;
    height: 300px;
    margin: -150px 0 0 -150px;
    border-radius: 50%;
    background: var(--monogram);
  }
  .contact {
    position: relative;
    display: flex;
    flex-direction: column;
    align-items: center;
  }
  .person-name {
    font-size: 28px;
    letter-spacing: 1px;
    margin-bottom: 34px;
  }
  .contact-line {
    font-size: 19px;
    letter-spacing: 0.5px;
    line-height: 30px;
  }
  .contact-line.address { margin-top: 14px; }
  .contact-line.website { margin-top: 14px; }
</style>
</head>
<body>
  <main class="sheet">
    <section class="card card-front" aria-label="Card front">
      <h1 class="brand-name">Marlowe Reed Fine Jewelry</h1>
      <div class="brand-rule"></div>
    </section>

    <section class="card card-back" aria-label="Card back">
      <div class="back-mark" aria-hidden="true"></div>
      <div class="contact">
        <p class="person-name">Lena Hartwell</p>
        <p class="contact-line phone">Phone: (555) 214-0386</p>
        <p class="contact-line email">lena.hartwell@example.com</p>
        <p class="contact-line address">482 Bayview Street, Harbor Point, FL 32999</p>
        <p class="contact-line website">www.marlowereedjewelry.com</p>
      </div>
    </section>
  </main>
</body>
</html>
```